Building company with a modern and unique product looking for a business card to help us stand out

We currently have a logo but as our business has grown, we feel that our business card is not reflecting our modern and high quality product and help us stand out from the crowd. Our business is mainly in the construction of new homes using a unique method and materials that makes our homes fire proof, vermin and pest resistant and rated to the maximum cyclone category (category 5). We need a business card that helps us stand out as well as communicating professionalism, high quality and trustworthiness. I have attached our current logo with a black and white option, as well as our business card which is double sided. We would like to retain as much of the information that is currently on our business cards, but presented in a more sleek way. We do like our current colour palette ( white, black, yellow and grey) and have been looking primarily at business cards with a black background however we are open to other combinations of colour and layout as long as we stand out. Please feel free to tweak our logo to make it more suitable for a business card, we like the black option that we use but we have had trouble trying to get the white area to match the rest of the logo and blend effectively into a business card. Please do not hesitate to contact us with any questions as we really want this to be successful!

Target Market(s)

Large contracts including government and larger companies

Industry/Entity Type

Business

We will be providing this business card to potential clients including key government ministers and large funding companies, our business card should show that we are professional and reliable.

Requirements
Must have
• It must be easy to read and pleasing to the eye, It must contain as much of the information on the current business card and unless something really stands out, we will most likely pick a design that has all of the information included. It must include our logo of course and have some colour included.
Nice to have
• We are looking for a high end business card and would like to see designs that reflect this. We like the gloss/matte contrast, plastic cards with opaque/coloured areas and unique features not seen on everyday paper business cards. It would be nice to see a few different colour combinations, we are open to new ideas so please feel free to take some artistic licence.
Should not have
• Must not be too busy, difficult to read or be distracting from the information conveyed. Other than this please feel free to add your own touches and make it unique!

```html
<!DOCTYPE html>
<html lang="en">
<head>
<meta charset="utf-8">
<title>Ridgeline Homes Co – Business Card</title>
<link href="https://fonts.googleapis.com/css2?family=Open+Sans:wght@400;600;700&display=swap" rel="stylesheet">
<style>
  :root {
    --ink: #0b0b0b;
    --gold: #d3ab2c;
    --paper: #ffffff;
    --stage: #e9e6df;
    --text-dark: #1c1a14;
    --text-soft: #4a4128;
  }
  * { box-sizing: border-box; margin: 0; padding: 0; }
  html, body {
    width: 1200px; height: 900px; overflow: hidden;
    background: var(--stage);
    font-family: "Open Sans", Arial, sans-serif;
  }
  .canvas { position: relative; width: 1200px; height: 900px; }

  .card {
    position: absolute;
    width: 580px; height: 330px;
    box-shadow: 0 10px 24px rgba(0,0,0,0.25);
    overflow: hidden;
  }

  /* Front */
  .card-front { left: 70px; top: 110px; background: var(--gold); }
  .front-band {
    position: absolute; inset: 0;
    background: var(--ink);
    clip-path: polygon(0 0, 100% 0, 100% 36%, 0 56%);
  }
  .brand {
    position: absolute;
    display: flex; align-items: center; gap: 8px;
    color: var(--gold); font-weight: 700;
    white-space: nowrap;
  }
  .brand-mark { background: var(--gold); flex: none; }
  .front-brand { left: 30px; top: 66px; font-size: 18px; }
  .front-brand .brand-mark { width: 14px; height: 14px; }

  .tagline {
    position: absolute; left: 290px; top: 36px;
    color: var(--paper); font-size: 14px; line-height: 1.35;
  }
  .tagline-lead { font-weight: 600; font-size: 15px; margin-bottom: 2px; }
  .tagline li { list-style: none; padding-left: 6px; }

  .person { position: absolute; left: 40px; top: 238px; color: var(--text-dark); }
  .person-name { font-size: 22px; letter-spacing: 1px; }
  .person-name strong { font-weight: 700; }
  .person-role { font-size: 14px; color: var(--text-soft); padding-left: 26px; letter-spacing: 0.5px; }

  .contacts { position: absolute; left: 290px; top: 192px; list-style: none; color: var(--text-dark); font-size: 14px; }
  .contacts li { display: flex; align-items: center; gap: 6px; margin-bottom: 5px; }
  .contacts svg { width: 18px; height: 18px; flex: none; }

  /* Back */
  .card-back {
    left: 560px; top: 490px; background: var(--ink);
    display: flex; align-items: center; justify-content: center;
  }
  .back-brand { position: static; font-size: 40px; gap: 14px; }
  .back-brand .brand-mark { width: 26px; height: 26px; }
</style>
</head>
<body>
<main class="canvas">

  <section class="card card-front" aria-label="Business card front">
    <div class="front-band"></div>
    <div class="brand front-brand"><span class="brand-mark"></span>Ridgeline Homes Co</div>

    <div class="tagline">
      <p class="tagline-lead">Specialising in Homes that are</p>
      <ul>
        <li>Fire Proof</li>
        <li>Climate Proof</li>
        <li>Cyclone Rated (Cat. 5)</li>
      </ul>
    </div>

    <ul class="contacts">
      <li>
        <svg viewBox="0 0 18 18"><circle cx="9" cy="9" r="9" fill="#0b0b0b"/><rect x="6.2" y="4" width="5.6" height="10" rx="1" fill="none" stroke="#d3ab2c" stroke-width="1.3"/><circle cx="9" cy="12" r="0.8" fill="#d3ab2c"/></svg>
        0400 123 456
      </li>
      <li>
        <svg viewBox="0 0 18 18"><circle cx="9" cy="9" r="9" fill="#0b0b0b"/><path d="M6 4.5c-.8.4-1.3 1.2-1 2.3.7 2.6 2.6 4.8 5.2 6 1 .4 1.9 0 2.4-.7l-1.6-1.7-1.2.6c-1-.6-1.8-1.5-2.3-2.6l.8-1.1z" fill="#d3ab2c"/></svg>
        (02) 5550 1234
      </li>
      <li>
        <svg viewBox="0 0 18 18"><circle cx="9" cy="9" r="9" fill="#0b0b0b"/><rect x="4.3" y="5.6" width="9.4" height="6.8" fill="none" stroke="#d3ab2c" stroke-width="1.2"/><path d="M4.5 6l4.5 3.6L13.5 6" fill="none" stroke="#d3ab2c" stroke-width="1.2"/></svg>
        hello@ridgelinehomes.com
      </li>
    </ul>

    <div class="person">
      <p class="person-name"><strong>Callum</strong> Reeves</p>
      <p class="person-role">Managing Director</p>
    </div>
  </section>

  <section class="card card-back" aria-label="Business card back">
    <div class="brand back-brand"><span class="brand-mark"></span>Ridgeline Homes Co</div>
  </section>

</main>
</body>
</html>
```